Delivery Performance Dashboard for Web Portal

We need you to design a dashboard for our web portal. We deliver sand and stone to construction jobsites. The attached screenshot is from our current web portal dashboard . It shows how much material has been delivered from an order.

Dump trucks will deliver multiple loads during the day and the dispatcher uses the dashboard to monitor if they need to add more trucks or less trucks to fulfill the order. An example would be, I need to ship 1,000 tons of sand to a jobsite and I plan to use 10 trucks during the day and that it will take 10 hours of hauling to complete the job. After 5 hours of hauling (50% the day is over), I should have delivered 500 tons of sand (50% of the order). But maybe there is a lot of traffic, and I only have delivered 300 tons. The dashboard will show that I am behind schedule and I might need to add 2 more trucks to the job.

Industry/Entity Type

Construction

Font styles to use
Sans Serif

Requirements
Must have
• We need a progress bar showing how much material has been delivered, how much material was requested to be delivered total and how much material should have been delivered at the current time. The goal is to show the user if the deliveries are ahead or behind the expected pace and why.
Nice to have
• The icons for plant, driving and jobsite show if the actual times have exceeded or beaten the planned times. Maybe you have other ideas to show the user if the trucks are sitting longer on the jobsite, at the plant to get loaded or driving to and from the jobsite.

```html
<!DOCTYPE html>
<html lang="en">
<head>
<meta charset="utf-8">
<title>Delivery Performance Dashboard</title>
<link href="https://fonts.googleapis.com/css2?family=Nunito+Sans:wght@400;600;700;800&display=swap" rel="stylesheet">
<style>
  :root{
    --brand:#2f3de8;
    --brand-soft:#e8eafd;
    --page:#f3f4f7;
    --panel:#ffffff;
    --ink:#1d1f2b;
    --ink-soft:#6b6f80;
    --line:#eceef3;
    --pending:#f6c343;
    --pending-soft:#fff4d6;
    --accepted:#22d3a0;
    --accepted-soft:#daf8ee;
    --ahead:#1fbf75;
    --behind:#ee4b5b;
    --track:#e6e8f2;
  }
  *{box-sizing:border-box;margin:0;padding:0}
  html,body{width:1200px;height:675px;overflow:hidden}
  body{font-family:"Nunito Sans",Arial,sans-serif;color:var(--ink);background:var(--page);display:flex}
  .sidebar{width:56px;background:var(--panel);display:flex;flex-direction:column;align-items:center;padding-top:14px;gap:14px;border-right:1px solid var(--line)}
  .brand-mark{width:28px;height:28px;border-radius:6px;background:var(--brand);margin-bottom:10px}
  .nav-item{width:30px;height:30px;border-radius:8px;display:flex;align-items:center;justify-content:center}
  .nav-item.is-active{background:var(--brand-soft)}
  .nav-item svg{width:14px;height:14px;stroke:var(--brand);fill:none;stroke-width:1.8}
  .main{flex:1;display:flex;flex-direction:column}
  .topbar{height:52px;background:var(--panel);display:flex;justify-content:flex-end;align-items:center;padding:0 28px;gap:8px;font-size:12px;font-weight:700}
  .avatar{width:24px;height:24px;border-radius:6px;background:#2a2c36}
  .caret{width:8px;height:8px;stroke:var(--ink-soft);fill:none;stroke-width:2}
  .content{padding:20px 24px;display:flex;flex-direction:column;gap:16px}
  .summary-row{display:flex;gap:16px}
  .summary-card{background:var(--panel);border-radius:10px;padding:14px 20px;display:flex;justify-content:space-between;align-items:flex-end;height:78px}
  .summary-card.pending{flex:1.5}
  .summary-card.travelers{flex:1}
  .summary-icon{width:22px;height:22px;border-radius:6px;display:flex;align-items:center;justify-content:center;margin-bottom:8px}
  .summary-icon span{width:8px;height:8px;border-radius:50%}
  .pending .summary-icon{background:var(--pending-soft)} .pending .summary-icon span{background:var(--pending)}
  .travelers .summary-icon{background:var(--accepted-soft)} .travelers .summary-icon span{background:var(--accepted)}
  .summary-label{font-size:13px;font-weight:800}
  .summary-value{font-size:18px;font-weight:800}
  .orders-panel{background:var(--panel);border-radius:10px;padding:6px 20px 14px}
  .orders-table{width:100%;border-collapse:collapse;font-size:10.5px}
  .orders-table th{text-align:left;font-size:11px;font-weight:800;padding:12px 6px 10px;border-bottom:1px solid var(--line)}
  .orders-table td{padding:0 6px;height:56px;border-bottom:1px solid var(--line);font-weight:600;vertical-align:middle}
  .orders-table tr:last-child td{border-bottom:none}
  .customer{color:var(--ink-soft)}
  .status{display:inline-block;padding:4px 10px;border-radius:12px;font-size:9.5px;font-weight:800;color:#fff}
  .status.pending{background:var(--pending)}
  .status.accepted{background:var(--accepted)}
  .tons-meta{display:flex;justify-content:space-between;font-size:9px;color:var(--ink-soft);margin-bottom:4px}
  .tons-bar{position:relative;height:6px;border-radius:3px;background:var(--track)}
  .tons-fill{position:absolute;left:0;top:0;bottom:0;border-radius:3px;background:var(--brand)}
  .tons-expected{position:absolute;top:-3px;width:2px;height:12px;border-radius:1px;background:var(--ink)}
  .tons-note{font-size:8.5px;margin-top:4px;font-weight:700}
  .ahead{color:var(--ahead)} .behind{color:var(--behind)}
  .wait-times{display:flex;gap:10px}
  .wait{display:flex;flex-direction:column;align-items:center;gap:2px;font-size:8.5px;font-weight:800}
  .wait svg{width:14px;height:14px;fill:currentColor}
  .remaining{font-weight:800;font-size:10.5px}
  .pagination{display:flex;justify-content:center;align-items:center;gap:10px;font-size:10px;font-weight:700;color:var(--ink-soft);padding-top:10px}
  .page-btn{width:22px;height:22px;border-radius:50%;display:flex;align-items:center;justify-content:center}
  .page-btn.prev{background:var(--line)}
  .page-btn.current{border:1.5px solid var(--brand);color:var(--brand)}
  .page-btn.next{background:var(--brand)}
  .page-btn svg{width:8px;height:8px;fill:none;stroke-width:2}
</style>
</head>
<body>
<svg width="0" height="0" style="position:absolute">
  <symbol id="icon-plant" viewBox="0 0 16 16"><path d="M1 15V7l4 2V7l4 2V3h3v12z"/></symbol>
  <symbol id="icon-truck" viewBox="0 0 16 16"><path d="M1 4h9v7H1zM10 7h3l2 2v2h-5z"/><circle cx="4" cy="12.5" r="1.6"/><circle cx="12" cy="12.5" r="1.6"/></symbol>
  <symbol id="icon-site" viewBox="0 0 16 16"><path d="M8 1a5 5 0 0 0-5 5c0 4 5 9 5 9s5-5 5-9a5 5 0 0 0-5-5zm0 7a2 2 0 1 1 0-4 2 2 0 0 1 0 4z"/></symbol>
</svg>

<aside class="sidebar">
  <div class="brand-mark"></div>
  <div class="nav-item is-active"><svg viewBox="0 0 16 16"><rect x="2" y="2" width="5" height="5"/><rect x="9" y="2" width="5" height="5"/><rect x="2" y="9" width="5" height="5"/><rect x="9" y="9" width="5" height="5"/></svg></div>
  <div class="nav-item"><svg viewBox="0 0 16 16"><circle cx="8" cy="5" r="3"/><path d="M2 15c0-3 3-5 6-5s6 2 6 5"/></svg></div>
  <div class="nav-item"><svg viewBox="0 0 16 16"><path d="M3 1h7l3 3v11H3z"/><path d="M6 8h5M6 11h5"/></svg></div>
  <div class="nav-item"><svg viewBox="0 0 16 16"><path d="M2 3h12v8H6l-4 3z"/></svg></div>
  <div class="nav-item"><svg viewBox="0 0 16 16"><path d="M3 15V2h9l-2 3 2 3H3"/></svg></div>
</aside>

<div class="main">
  <header class="topbar">
    <div class="avatar"></div>
    <span>Dana Keller</span>
    <svg class="caret" viewBox="0 0 8 8"><path d="M1 2.5l3 3 3-3"/></svg>
  </header>

  <main class="content">
    <section class="summary-row">
      <div class="summary-card pending">
        <div><div class="summary-icon"><span></span></div><div class="summary-label">Pending Orders</div></div>
        <div class="summary-value">05</div>
      </div>
      <div class="summary-card travelers">
        <div><div class="summary-icon"><span></span></div><div class="summary-label">Active Travelers</div></div>
        <div class="summary-value">345</div>
      </div>
    </section>

    <section class="orders-panel">
      <table class="orders-table">
        <thead>
          <tr><th style="width:58px">Order #</th><th style="width:150px">Origin</th><th style="width:170px">Destination</th><th style="width:200px">Customer</th><th style="width:86px">Status</th><th style="width:160px">Tons</th><th style="width:150px">Wait Times</th><th>Remaining</th></tr>
        </thead>
        <tbody>
          <tr>
            <td>2499</td><td>Ridgeway Asphalt Plant</td><td>BZV3 - 185 from mm 77 - 96</td><td class="customer">Harlow Construction - North Division</td>
            <td><span class="status pending">Pending</span></td>
            <td><div class="tons-meta"><span>10 / 1000</span><span>07:30 - 17:30</span></div><div class="tons-bar"><div class="tons-fill" style="width:2%"></div><div class="tons-expected" style="left:4%"></div></div><div class="tons-note" style="color:var(--ink-soft)">Not started</div></td>
            <td><div class="wait-times"><span class="wait" style="color:var(--ink-soft)"><svg><use href="#icon-plant"/></svg>--</span><span class="wait" style="color:var(--ink-soft)"><svg><use href="#icon-truck"/></svg>--</span><span class="wait" style="color:var(--ink-soft)"><svg><use href="#icon-site"/></svg>--</span></div></td>
            <td class="remaining">10 hrs</td>
          </tr>
          <tr>
            <td>3715</td><td>Brookfield Asphalt Plant</td><td>Oak Springs</td><td class="customer">Harlow Construction - North Division</td>
            <td><span class="status accepted">Accepted</span></td>
            <td><div class="tons-meta"><span>700 / 1000</span><span>07:00 - 17:00</span></div><div class="tons-bar"><div class="tons-fill" style="width:70%"></div><div class="tons-expected" style="left:60%"></div></div><div class="tons-note ahead">+100 t ahead</div></td>
            <td><div class="wait-times"><span class="wait ahead"><svg><use href="#icon-plant"/></svg>8m</span><span class="wait ahead"><svg><use href="#icon-truck"/></svg>22m</span><span class="wait ahead"><svg><use href="#icon-site"/></svg>9m</span></div></td>
            <td class="remaining ahead">+1 hrs</td>
          </tr>
          <tr>
            <td>4860</td><td>Ridgeway Asphalt Plant</td><td>BZV3 - 185 from mm 77 - 96</td><td class="customer">Harlow Construction - North Division</td>
            <td><span class="status accepted">Accepted</span></td>
            <td><div class="tons-meta"><span>300 / 1000</span><span>07:30 - 17:30</span></div><div class="tons-bar"><div class="tons-fill" style="width:30%"></div><div class="tons-expected" style="left:50%"></div></div><div class="tons-note behind">-200 t behind</div></td>
            <td><div class="wait-times"><span class="wait ahead"><svg><use href="#icon-plant"/></svg>9m</span><span class="wait behind"><svg><use href="#icon-truck"/></svg>41m</span><span class="wait ahead"><svg><use href="#icon-site"/></svg>10m</span></div></td>
            <td class="remaining behind">-02:00 Hrs</td>
          </tr>
          <tr>
            <td>1612</td><td>Stonebay Asphalt Plant</td><td>A45, Elm Loop, Westfield</td><td class="customer">Harlow Construction - North Division</td>
            <td><span class="status accepted">Accepted</span></td>
            <td><div class="tons-meta"><span>580 / 1000</span><span>07:00 - 17:00</span></div><div class="tons-bar"><div class="tons-fill" style="width:58%"></div><div class="tons-expected" style="left:55%"></div></div><div class="tons-note ahead">+30 t ahead</div></td>
            <td><div class="wait-times"><span class="wait ahead"><svg><use href="#icon-plant"/></svg>7m</span><span class="wait ahead"><svg><use href="#icon-truck"/></svg>25m</span><span class="wait behind"><svg><use href="#icon-site"/></svg>18m</span></div></td>
            <td class="remaining ahead">+0:20 Hrs</td>
          </tr>
          <tr>
            <td>800</td><td>Ridgeway Asphalt Plant</td><td>Oak Springs</td><td class="customer">Harlow Construction - North Division</td>
            <td><span class="status accepted">Accepted</span></td>
            <td><div class="tons-meta"><span>450 / 1000</span><span>07:30 - 17:30</span></div><div class="tons-bar"><div class="tons-fill" style="width:45%"></div><div class="tons-expected" style="left:45%"></div></div><div class="tons-note" style="color:var(--ink-soft)">On pace</div></td>
            <td><div class="wait-times"><span class="wait ahead"><svg><use href="#icon-plant"/></svg>8m</span><span class="wait ahead"><svg><use href="#icon-truck"/></svg>24m</span><span class="wait ahead"><svg><use href="#icon-site"/></svg>9m</span></div></td>
            <td class="remaining ahead">0:00 Hrs</td>
          </tr>
          <tr>
            <td>3236</td><td>Brookfield Asphalt Plant</td><td>Oak Springs</td><td class="customer">Harlow Construction - North Division</td>
            <td><span class="status accepted">Accepted</span></td>
            <td><div class="tons-meta"><span>420 / 1000</span><span>07:00 - 17:00</span></div><div class="tons-bar"><div class="tons-fill" style="width:42%"></div><div class="tons-expected" style="left:50%"></div></div><div class="tons-note behind">-80 t behind</div></td>
            <td><div class="wait-times"><span class="wait behind"><svg><use href="#icon-plant"/></svg>15m</span><span class="wait ahead"><svg><use href="#icon-truck"/></svg>23m</span><span class="wait ahead"><svg><use href="#icon-site"/></svg>8m</span></div></td>
            <td class="remaining behind">-00:20 Hrs</td>
          </tr>
        </tbody>
      </table>

      <nav class="pagination">
        <span class="page-btn prev"><svg viewBox="0 0 8 8" stroke="#9aa0b2"><path d="M5 1L2 4l3 3"/></svg></span>
        <span class="page-btn current">01</span>
        <span>02</span><span>03</span><span>…</span><span>10</span>
        <span class="page-btn next"><svg viewBox="0 0 8 8" stroke="#fff"><path d="M3 1l3 3-3 3"/></svg></span>
      </nav>
    </section>
  </main>
</div>
</body>
</html>
```